CRPG is needing business cards, and stationary created.

Pixel Forge created a logo for our business, and now we are wanting business cards, and stationary. I have included two designs of the same logo. Please feel free to use them as you want. The name of the company is Cedar Ridge Property Group LLC, the address is 812 NE Tamber Ln., Suite 9, the city & state is Bend, Oregon, zip code is 97815, Telephone number is 541-237-4190, Fax number is 541-237-8856, the name on the business card is Travis Lundqor CMCA

Industry/Entity Type

Property Management

Contact Information for Business Card

The card needs to look professional. Upscale.

Requirements
Must have
• The colors we are using are on the logo that has been uploaded.

```html
<!DOCTYPE html>
<html lang="en">
<head>
<meta charset="utf-8">
<title>Cedar Ridge Property Group – Business Card</title>
<link rel="stylesheet" href="https://fonts.googleapis.com/css2?family=Noto+Sans:wght@300;400;700&display=swap">
<style>
  :root {
    --backdrop: #3f424a;
    --paper: #fbfbfb;
    --navy: #344254;
    --navy-deep: #2f3b4b;
    --teal: #14866d;
    --teal-bright: #1a9a7c;
    --teal-faint: #d6ebe8;
    --text-light: #f2f4f6;
  }
  html, body {
    margin: 0;
    width: 1200px;
    height: 675px;
    overflow: hidden;
    background: var(--backdrop);
  }
  .canvas {
    width: 1200px;
    height: 675px;
    display: flex;
    align-items: center;
    justify-content: center;
  }
  .card {
    width: 340px;
    height: 595px;
    background: var(--paper);
    display: flex;
    flex-direction: column;
    font-family: "Noto Sans", sans-serif;
    box-shadow: 0 10px 30px rgba(0,0,0,0.35);
  }
  .card-top {
    height: 290px;
    position: relative;
    overflow: hidden;
  }
  .brand {
    position: absolute;
    top: 58px;
    left: 0;
    right: 0;
    display: flex;
    align-items: center;
    justify-content: center;
    gap: 10px;
  }
  .brand-square {
    width: 22px;
    height: 22px;
    background: var(--teal);
  }
  .brand-name {
    font-weight: 700;
    font-size: 30px;
    color: var(--teal);
    letter-spacing: 0.5px;
    text-transform: uppercase;
  }
  .brand-watermark {
    position: absolute;
    bottom: -14px;
    left: 0;
    right: 0;
    text-align: center;
    font-weight: 700;
    font-size: 118px;
    color: var(--teal-faint);
    line-height: 1;
  }
  .accent-rule {
    height: 6px;
    background: var(--teal-bright);
  }
  .card-bottom {
    flex: 1;
    background: linear-gradient(180deg, var(--navy) 0%, var(--navy-deep) 100%);
    color: var(--text-light);
    text-align: center;
    padding-top: 58px;
    box-sizing: border-box;
  }
  .person-name {
    font-weight: 300;
    font-size: 27px;
    margin: 0;
    line-height: 1.2;
  }
  .person-title {
    font-weight: 300;
    font-size: 27px;
    color: var(--teal-bright);
    margin: 0 0 20px;
    line-height: 1.2;
  }
  .address {
    font-weight: 400;
    font-size: 13.5px;
    line-height: 1.45;
    margin: 0 22px;
  }
  .divider {
    height: 1px;
    margin: 12px 40px 12px;
    background: linear-gradient(90deg, transparent, var(--teal) 50%, transparent);
  }
  .contact {
    font-weight: 400;
    font-size: 13.5px;
    line-height: 1.6;
    margin: 0;
  }
</style>
</head>
<body>
  <main class="canvas">
    <article class="card">
      <section class="card-top">
        <div class="brand">
          <span class="brand-square"></span>
          <span class="brand-name">Cedar Ridge</span>
        </div>
        <div class="brand-watermark" aria-hidden="true">CRPG</div>
      </section>
      <div class="accent-rule"></div>
      <section class="card-bottom">
        <p class="person-name">Travis Lundqor</p>
        <p class="person-title">CMCA</p>
        <p class="address">Cedar Ridge Property Group LLC,<br>812 NE Tamber Ln., Suite 9, the city &amp; state is Bend,<br>Oregon, zip code 97815</p>
        <div class="divider"></div>
        <p class="contact">Telephone: 541-237-4190<br>Fax: 541-237-8856</p>
      </section>
    </article>
  </main>
</body>
</html>
```